New Look Driving School Project

Current website:
www. pelmarsteeracademy.com

Websites that we like (use content and courses from here as well):
https://www. quorbeltlessons.com

We are looking for a fresh looking driving school website that is easy for students to find the course they are looking for, the price, and allow them to book a lesson all on our website. We would like for this website to have multiple pages: Home, Teen Courses, Adult Courses, About Us, Contact, FAQ, Blog, Requirements.

Target Market(s)

Students in High School or Parents

Industry/Entity Type

Education

Coding

Coded - Design and coding required

Number of Pages Required

5+ page

Font styles to use
Serif
Sans Serif

Colors

Designer to choose colors to be used in the design.

Requirements
Must have
• Must have a form submission and payment processing option. Must have the ability to pick a course, see available times, and process their payment online. MUST BE MOBILE FRIENDLY DESIGN.
Nice to have
• Nice to have a clean format, with big bold fonts.
Should not have
• Should not have a lot of sliders or animations. Should be very fast loading on mobile. Keep it simple but easy to read and elegant.

```html
<!DOCTYPE html>
<html lang="en">
<head>
<meta charset="utf-8">
<title>Pelmar Steer Academy</title>
<link href="https://fonts.googleapis.com/css2?family=Poppins:wght@400;500;600;700&display=swap" rel="stylesheet">
<style>
:root{
  --red:#e8112d;
  --red-dark:#c70c24;
  --ink:#222;
  --muted:#555;
  --grey:#ececec;
  --dark:#1c1c1c;
  --white:#fff;
}
*{box-sizing:border-box;margin:0;padding:0}
html,body{width:1200px;height:4072px;overflow:hidden}
body{font-family:'Poppins',sans-serif;color:var(--ink);background:var(--white);position:relative}
section,header,footer{position:absolute;left:0;width:1200px}
.abs{position:absolute}
svg{display:block}

/* top bar */
.topbar{top:0;height:38px;font-size:13px;color:#333}
.topbar .item{position:absolute;top:11px;display:flex;align-items:center;gap:6px}
.topbar .dot{width:10px;height:10px;background:var(--red);border-radius:50%}
.topbar .sq{width:13px;height:13px;background:var(--red);border-radius:2px}

/* header */
.header{top:38px;height:138px;background:var(--red);color:var(--white)}
.brand{left:90px;top:48px;font-size:36px;font-weight:500}
.support{left:703px;top:22px;display:flex;align-items:center;gap:10px}
.support .ico{width:38px;height:38px;border-radius:50%;border:2px solid #fff;display:flex;align-items:center;justify-content:center}
.support small{display:block;font-size:14px}
.support b{font-size:20px;font-weight:600}
.book{left:915px;top:30px;width:196px;height:46px;border:2px solid #fff;border-radius:24px;font-size:15px;font-weight:600;display:flex;align-items:center;justify-content:center;gap:8px}
.nav{left:430px;top:98px;display:flex;gap:24px;font-size:16px}

/* hero */
.hero{top:176px;height:503px;background:linear-gradient(180deg,#2a3a6a 0%,#8a5a8a 40%,#d06a5a 62%,#2a2f55 80%,#141a30 100%)}
.offer{left:89px;top:244px;width:408px;height:408px;border-radius:50%;background:var(--red);display:flex;align-items:center;justify-content:center}
.offer-in{width:364px;height:364px;border-radius:50%;background:rgba(20,20,20,.92);color:#fff;text-align:center;padding-top:88px}
.offer-in h2{font-size:35px;font-weight:500}
.offer-in p{font-size:18px;margin-top:8px}
.offer-in .pct{font-size:40px;font-weight:600;margin-top:2px}
.offer-in .ph{font-size:29px;margin-top:2px;display:flex;justify-content:center;align-items:center;gap:8px}
.offer-in .btn{display:inline-block;margin-top:18px;background:var(--red);padding:10px 30px;border-radius:24px;font-size:18px;font-weight:600}

.stats{top:679px;height:108px;background:rgba(25,25,25,.9);color:#fff}
.stat{position:absolute;top:22px}
.stat b{font-size:36px;font-weight:600;display:flex;align-items:center;gap:14px}
.stat span{font-size:15px;font-weight:600;display:block;margin-top:-4px}

/* form card */
.finder{left:782px;top:217px;width:339px;height:630px;background:#fff;box-shadow:0 2px 12px rgba(0,0,0,.25);padding:18px 15px}
.finder h3{font-size:25px;font-weight:600;color:var(--ink)}
.finder h3 em{font-style:normal;color:var(--red);font-weight:500}
.finder .lead{font-size:14px;line-height:1.6;margin-top:4px}
.fld{height:44px;border:2px solid var(--red);display:flex;align-items:center;margin-top:18px;font-size:13px;color:#999}
.fld .ic{width:40px;height:100%;background:var(--red);display:flex;align-items:center;justify-content:center;margin-right:12px}
.row2{display:flex;gap:24px}
.row2 .fld{flex:1}
.reg{margin-top:20px;height:44px;background:var(--red);color:#fff;font-size:12px;font-weight:600;display:flex;align-items:center;justify-content:center}
.finder .q{font-size:14px;line-height:1.65;margin-top:16px}
.finder .q b{font-weight:600}
.finder .call{color:var(--red);font-size:14px;margin-top:10px}

/* about */
.about{top:870px;height:506px}
.hex{left:109px;top:48px}
.about-txt{left:567px;top:48px;width:525px}
.about-txt h2{font-size:34px;font-weight:500;color:var(--red)}
.about-txt .lead{font-size:14px;font-weight:600;line-height:1.8;margin-top:10px}
.about-txt p{font-size:13px;line-height:1.85;margin-top:12px;color:#333}
.btn-red{display:inline-flex;align-items:center;gap:8px;background:var(--red);color:#fff;font-size:16px;font-weight:600;padding:13px 26px;border-radius:30px;margin-top:28px}

/* advanced */
.advanced{top:1376px;height:497px;background:var(--grey);text-align:center}
.advanced h2{font-size:36px;font-weight:600;color:var(--red);margin-top:62px}
.advanced .sub{font-size:17px;line-height:1.8;width:1040px;margin:16px auto 0;color:#444}
.feats{display:flex;justify-content:center;gap:75px;margin-top:58px}
.feat{width:290px}
.feat .dia{width:76px;height:76px;background:#fff;transform:rotate(45deg);margin:0 auto;display:flex;align-items:center;justify-content:center}
.feat .dia svg{transform:rotate(-45deg)}
.feat h4{font-size:17px;color:var(--red);font-weight:600;margin-top:28px}
.feat p{font-size:14px;line-height:1.85;margin-top:10px;color:#333}

/* courses */
.courses{top:1873px;height:435px;background:linear-gradient(180deg,#2e2b2a,#1f1d1c 60%,#262220);color:#fff;text-align:center}
.courses h2{font-size:34px;font-weight:600;margin-top:64px}
.courses .sub{font-size:14px;line-height:2;width:1000px;margin:18px auto 0}
.ccard{position:absolute;top:234px;width:324px;height:127px;background:#fff;color:var(--ink);text-align:left;display:flex;padding:18px 12px}
.ccard .wheel{width:74px;height:74px;border:3px solid var(--red);border-radius:50%;flex:none;display:flex;align-items:center;justify-content:center;margin-top:8px}
.ccard h4{font-size:15px;color:var(--red);font-weight:600;margin-left:14px}
.ccard p{font-size:12px;line-height:1.75;margin:6px 0 0 14px}

/* blog */
.blog{top:2308px;height:630px;background:var(--grey)}
.blog h2{text-align:center;font-size:36px;font-weight:600;color:var(--red);margin-top:98px}
.post{position:absolute;top:157px;width:328px}
.post .ph{height:196px}
.post .date{position:absolute;left:18px;top:172px;background:var(--red);color:#fff;font-size:13px;padding:6px 14px;display:flex;gap:6px;align-items:center}
.post h4{font-size:19px;font-weight:600;color:var(--red);margin-top:40px}
.post p{font-size:13px;line-height:1.85;margin-top:8px}
.post .more{font-size:13px;color:var(--red);font-weight:600;margin-top:14px}

/* contact */
.contact{top:2938px;height:822px;text-align:center}
.contact h2{font-size:36px;font-weight:500;color:var(--red);margin-top:78px}
.contact .sub{font-size:20px;font-weight:500;margin-top:4px;color:#333}
.cinfo{display:flex;justify-content:center;gap:140px;margin-top:30px}
.ci{width:260px}
.ci .circ{width:86px;height:86px;border-radius:50%;background:var(--red);margin:0 auto;display:flex;align-items:center;justify-content:center}
.ci p{font-size:17px;color:#444;line-height:1.55;margin-top:18px}
.ci b{font-size:19px;font-weight:600;color:var(--ink)}
.contact h3{font-size:36px;font-weight:500;color:var(--red);margin-top:26px}
.cform{position:absolute;left:163px;top:456px;width:877px}
.inp{position:absolute;height:48px;border:1px solid #eee;box-shadow:0 1px 3px rgba(0,0,0,.12);font-size:13px;color:#555;text-align:left;padding:15px 14px}
.submit{position:absolute;left:518px;top:708px;width:166px;height:46px;border-radius:24px;background:var(--red);color:#fff;font-size:17px;font-weight:600;display:flex;align-items:center;justify-content:center;gap:8px}

/* footer */
.footer{top:3760px;height:312px;background:var(--dark);color:#fff;text-align:center}
.footer h2{font-size:42px;font-weight:500;margin-top:50px}
.socials{display:flex;justify-content:center;gap:8px;margin-top:14px}
.socials span{width:30px;height:30px;border:2px solid #fff;border-radius:50%}
.flinks{font-size:15px;margin-top:24px}
.flinks + .flinks{margin-top:22px}
.copy{font-size:13px;color:#bbb;margin-top:22px}
</style>
</head>
<body>

<header class="topbar">
  <div class="item" style="left:98px"><span class="dot"></span>Brookvale</div>
  <div class="item" style="left:185px"><span class="dot"></span>info@pelmarsteeracademy.com</div>
  <div class="item" style="left:395px"><span class="dot"></span>555-014-2290</div>
  <div class="item" style="left:758px"><span class="dot"></span>Opening Hours: Mon - Fri 9:00 A.M - 7:00 P.M</div>
  <div class="item" style="left:1072px"><span class="sq"></span><span class="sq"></span></div>
</header>

<header class="header">
  <div class="abs brand">Pelmar Steer Academy</div>
  <div class="abs support">
    <span class="ico"><svg width="18" height="18" viewBox="0 0 24 24"><path fill="#fff" d="M6.6 10.8a15 15 0 0 0 6.6 6.6l2.2-2.2c.3-.3.7-.4 1-.2 1.1.4 2.3.6 3.6.6.6 0 1 .4 1 1V20c0 .6-.4 1-1 1A17 17 0 0 1 3 4c0-.6.4-1 1-1h3.5c.6 0 1 .4 1 1 0 1.3.2 2.5.6 3.6.1.3 0 .7-.2 1z"/></svg></span>
    <div><small>Support Call us</small><b>555-014-7731</b></div>
  </div>
  <div class="abs book"><svg width="16" height="16" viewBox="0 0 24 24"><rect x="3" y="5" width="18" height="16" rx="2" fill="none" stroke="#fff" stroke-width="2"/><path d="M3 10h18M8 3v4M16 3v4" stroke="#fff" stroke-width="2"/></svg>BOOK A LESSON</div>
  <nav class="abs nav"><span>Teen Courses</span><span>Adult Courses</span><span>About</span><span>Contact</span><span>FAQ</span><span>Blog</span><span>Requirements</span></nav>
</header>

<section class="hero" role="img" aria-label="City skyline along a river at dusk"></section>
<div class="abs offer">
  <div class="offer-in">
    <h2>Pelmar Steer Academy</h2>
    <p>Get Your First Lesson… for</p>
    <div class="pct">5% off</div>
    <div class="ph"><svg width="24" height="24" viewBox="0 0 24 24"><path fill="#fff" d="M6.6 10.8a15 15 0 0 0 6.6 6.6l2.2-2.2c.3-.3.7-.4 1-.2 1.1.4 2.3.6 3.6.6.6 0 1 .4 1 1V20c0 .6-.4 1-1 1A17 17 0 0 1 3 4c0-.6.4-1 1-1h3.5c.6 0 1 .4 1 1 0 1.3.2 2.5.6 3.6.1.3 0 .7-.2 1z"/></svg>555-014-7731</div>
    <span class="btn">Avail Offers</span>
  </div>
</div>

<section class="stats">
  <div class="stat" style="left:90px"><b>20,000 <svg width="46" height="46" viewBox="0 0 24 24"><circle cx="12" cy="12" r="10" fill="none" stroke="#fff" stroke-width="2.4"/><path d="M12 6v6l4 2" stroke="#fff" stroke-width="2.4" fill="none"/></svg></b><span>HOURS OF TEACHING</span></div>
  <div class="stat" style="left:340px"><b>100% <svg width="46" height="46" viewBox="0 0 24 24"><path fill="#fff" d="M2 10h4v11H2zM8 21V10l5-8c1.5 0 2.5 1 2.3 2.5L14.5 9H21c1 0 1.8 1 1.6 2l-1.6 8c-.2 1.2-1.2 2-2.4 2z"/></svg></b><span>SATISFACTION</span></div>
  <div class="stat" style="left:582px"><b>FREE <svg width="50" height="44" viewBox="0 0 24 20"><path fill="#fff" d="M4 8l2-5h12l2 5h2v7h-2v3h-3v-3H7v3H4v-3H2V8zm3-3l-1.3 3h12.6L17 5zM6 10.5a1.5 1.5 0 1 0 0 3 1.5 1.5 0 0 0 0-3zm12 0a1.5 1.5 0 1 0 0 3 1.5 1.5 0 0 0 0-3z"/></svg></b><span>PICK UP AND DROP OFF</span></div>
</section>

<aside class="abs finder">
  <h3>FIND <em>DRIVING COURSES</em></h3>
  <p class="lead">Send us your details and we'll find the best schedule for you!</p>
  <div class="fld"><span class="ic"><svg width="16" height="16" viewBox="0 0 24 24"><circle cx="12" cy="8" r="4" fill="#fff"/><path d="M4 21c0-4.5 3.5-7 8-7s8 2.5 8 7z" fill="#fff"/></svg></span>User Name</div>
  <div class="fld"><span class="ic"><svg width="16" height="14" viewBox="0 0 24 18"><rect width="24" height="18" rx="2" fill="#fff"/><path d="M1 2l11 8 11-8" stroke="#e8112d" stroke-width="2" fill="none"/></svg></span>Email</div>
  <div class="fld"><span class="ic"><svg width="16" height="16" viewBox="0 0 24 24"><path fill="#fff" d="M6.6 10.8a15 15 0 0 0 6.6 6.6l2.2-2.2c.3-.3.7-.4 1-.2 1.1.4 2.3.6 3.6.6.6 0 1 .4 1 1V20c0 .6-.4 1-1 1A17 17 0 0 1 3 4c0-.6.4-1 1-1h3.5c.6 0 1 .4 1 1 0 1.3.2 2.5.6 3.6.1.3 0 .7-.2 1z"/></svg></span>Phone Number</div>
  <div class="row2">
    <div class="fld"><span class="ic"><svg width="14" height="18" viewBox="0 0 24 32"><path fill="#fff" d="M12 0a12 12 0 0 0-12 12c0 9 12 20 12 20s12-11 12-20A12 12 0 0 0 12 0zm0 17a5 5 0 1 1 0-10 5 5 0 0 1 0 10z"/></svg></span>City</div>
    <div class="fld"><span class="ic"><svg width="16" height="16" viewBox="0 0 24 24"><rect x="3" y="5" width="18" height="16" rx="2" fill="#fff"/><path d="M3 10h18" stroke="#e8112d" stroke-width="2"/></svg></span>Age</div>
  </div>
  <div class="fld"><span class="ic"><svg width="16" height="16" viewBox="0 0 24 24"><circle cx="12" cy="12" r="9" fill="none" stroke="#fff" stroke-width="3"/><circle cx="12" cy="12" r="2.5" fill="#fff"/></svg></span>Course<span style="margin-left:auto;margin-right:14px;color:#777">▾</span></div>
  <div class="reg">REGISTER + PAY LATER</div>
  <p class="q"><b>Questions about pricing or schedules?</b><br>Call us and we will help you navigate through the process and answer all of your questions!</p>
  <p class="call">Call: 555-014-7731</p>
</aside>

<section class="about">
  <svg class="abs hex" width="434" height="380" viewBox="0 0 434 380">
    <polygon points="108,4 326,4 430,190 326,376 108,376 4,190" fill="none" stroke="#e8112d" stroke-width="4"/>
    <polygon points="116,18 318,18 414,190 318,362 116,362 20,190" fill="#c9a86a"/>
  </svg>
  <div class="abs" role="img" aria-label="Yellow road warning signs for cyclists and pedestrians" style="left:129px;top:66px;width:394px;height:344px;clip-path:polygon(24% 0,76% 0,100% 50%,76% 100%,24% 100%,0 50%);background:linear-gradient(135deg,#e5d7a8,#d9a23a 45%,#b67a3a 70%,#efe7cf)"></div>
  <div class="abs about-txt">
    <h2>About Pelmar Steer Academy</h2>
    <p class="lead">We are experts in teen driving education in Brookvale, Elmridge, Carrow Heights, and Dunmore and the greater North County area.</p>
    <p>Pelmar Steer Academy specializes in Behind the Wheel for Teens and Adults, Learners Permits, and Drivers Education. Sed ut perspiciatis unde omnis iste natus error sit voluptatem accusantium doloremque laudantium, totam rem aperiam, eaque ipsa quae ab illo inventore veritatis et quasi architecto beatae vitae dicta sunt explicabo. Nemo enim ipsam voluptatem quia voluptas sit aspernatur aut odit aut fugit, quia ratione voluptatem sequi nesciunt.</p>
    <span class="btn-red">READ MORE <svg width="16" height="16" viewBox="0 0 24 24"><circle cx="12" cy="12" r="11" fill="#fff"/><path d="M10 7l5 5-5 5" stroke="#e8112d" stroke-width="3" fill="none"/></svg></span>
  </div>
</section>

<section class="advanced">
  <h2>The Most Advanced Driving School in North County</h2>
  <p class="sub">Sed ut perspiciatis unde omnis iste natus error sit voluptatem accusantium doloremque laudantium, totam rem aperiam, eaque ipsa quae explicabo.</p>
  <div class="feats">
    <div class="feat"><div class="dia"><svg width="34" height="34" viewBox="0 0 24 24"><circle cx="12" cy="12" r="7" fill="none" stroke="#e8112d" stroke-width="4" stroke-dasharray="3 2.5"/><circle cx="12" cy="12" r="5" fill="#e8112d"/><circle cx="12" cy="12" r="2" fill="#fff"/></svg></div><h4>AFFORDABLE</h4><p>You have nothing to worry about, as our services are affordable and flexible.</p></div>
    <div class="feat"><div class="dia"><svg width="34" height="34" viewBox="0 0 24 24"><circle cx="12" cy="12" r="11" fill="#e8112d"/><path d="M7 12l3.5 3.5L17 9" stroke="#fff" stroke-width="2.5" fill="none"/></svg></div><h4>GUARANTEE</h4><p>We guarantee 100% satisfaction and premium training from our instructors</p></div>
    <div class="feat"><div class="dia"><svg width="34" height="34" viewBox="0 0 24 24"><path fill="#e8112d" d="M12 2a10 10 0 0 0 0 20c1.5 0 2-1 2-2 0-1.5-1-1.7-1-3 0-1 .8-2 2-2h2a5 5 0 0 0 5-5c0-4.4-4.5-8-10-8z"/><circle cx="7" cy="11" r="1.6" fill="#fff"/><circle cx="10" cy="7" r="1.6" fill="#fff"/><circle cx="15" cy="7" r="1.6" fill="#fff"/></svg></div><h4>EXPERIENCE</h4><p>We offer private 1-on-1 lessons and customize training</p></div>
  </div>
</section>

<section class="courses" role="region" aria-label="Our Courses">
  <h2>Our Courses</h2>
  <p class="sub">Sed ut perspiciatis unde omnis iste natus error sit voluptatem accusantium doloremque laudantium, totam rem aperiam, eaque ipsa quae ab illo inventore veritatis et quasi architecto beatae vitae dicta sunt explicabo. Nemo enim ipsam voluptatem quia voluptas sit aspernatur aut odit aut fugit, sed quia consequuntur magni dolores eos qui ratione voluptatem sequi nesciunt.</p>
  <div class="ccard" style="left:100px"><span class="wheel"><svg width="50" height="50" viewBox="0 0 24 24"><circle cx="12" cy="12" r="10" fill="none" stroke="#e8112d" stroke-width="2"/><circle cx="12" cy="12" r="2.5" fill="none" stroke="#e8112d" stroke-width="2"/><path d="M2.5 10.5h7M14.5 10.5h7M12 14.5V22" stroke="#e8112d" stroke-width="2"/></svg></span><div><h4>Behind The Wheel $250</h4><p>Sed ut perspiciatis unde omnis iste natus error sit voluptatem accusan laudantium, totam rem aperiam</p></div></div>
  <div class="ccard" style="left:437px"><span class="wheel"><svg width="50" height="50" viewBox="0 0 24 24"><circle cx="12" cy="12" r="10" fill="none" stroke="#e8112d" stroke-width="2"/><circle cx="12" cy="12" r="2.5" fill="none" stroke="#e8112d" stroke-width="2"/><path d="M2.5 10.5h7M14.5 10.5h7M12 14.5V22" stroke="#e8112d" stroke-width="2"/></svg></span><div><h4>Private 1 on 1 Driving $400</h4><p>Sed ut perspiciatis unde omnis iste natus error sit voluptatem accusan laudantium, totam rem aperiam</p></div></div>
  <div class="ccard" style="left:776px"><span class="wheel"><svg width="50" height="50" viewBox="0 0 24 24"><circle cx="12" cy="12" r="10" fill="none" stroke="#e8112d" stroke-width="2"/><circle cx="12" cy="12" r="2.5" fill="none" stroke="#e8112d" stroke-width="2"/><path d="M2.5 10.5h7M14.5 10.5h7M12 14.5V22" stroke="#e8112d" stroke-width="2"/></svg></span><div><h4>60 Days Waver Package $600</h4><p>Sed ut perspiciatis unde omnis iste natus error sit voluptatem accusan laudantium, totam rem aperiam</p></div></div>
</section>

<section class="blog">
  <h2>Our Blog</h2>
  <article class="post" style="left:95px">
    <div class="ph" role="img" aria-label="Instructor beside a white car with a traffic cone" style="background:linear-gradient(135deg,#5a6470,#c9ced4 55%,#8f969c)"></div>
    <span class="date"><svg width="12" height="12" viewBox="0 0 24 24"><rect x="3" y="5" width="18" height="16" rx="2" fill="#fff"/></svg>Oct 27 2018</span>
    <h4>SED UT PERSPICIATIS UND</h4><p>Sed ut perspiciatis unde omnis iste natus error sit voluptatem accusantium doloremque laudantium, totam rem aperiam, eaque ipsa quae ab illo</p><p class="more">READ MORE</p>
  </article>
  <article class="post" style="left:437px">
    <div class="ph" role="img" aria-label="Rows of orange traffic cones on a practice lot" style="background:linear-gradient(180deg,#5c7a4a,#8a8a80 45%,#d9542a 75%,#6c6c6c)"></div>
    <span class="date"><svg width="12" height="12" viewBox="0 0 24 24"><rect x="3" y="5" width="18" height="16" rx="2" fill="#fff"/></svg>Oct 27 2018</span>
    <h4>SED UT PERSPICIATIS UND</h4><p>Sed ut perspiciatis unde omnis iste natus error sit voluptatem accusantium doloremque laudantium, totam rem aperiam, eaque ipsa quae ab illo</p><p class="more">READ MORE</p>
  </article>
  <article class="post" style="left:777px">
    <div class="ph" role="img" aria-label="Yellow road warning signs against the sky" style="background:linear-gradient(135deg,#efe6d0,#dcae3e 50%,#b07a3a)"></div>
    <span class="date"><svg width="12" height="12" viewBox="0 0 24 24"><rect x="3" y="5" width="18" height="16" rx="2" fill="#fff"/></svg>Oct 27 2018</span>
    <h4>SED UT PERSPICIATIS UND</h4><p>Sed ut perspiciatis unde omnis iste natus error sit voluptatem accusantium doloremque laudantium, totam rem aperiam, eaque ipsa quae ab illo</p><p class="more">READ MORE</p>
  </article>
</section>

<section class="contact">
  <h2>Contact Information</h2>
  <p class="sub">Contact us for more information</p>
  <div class="cinfo">
    <div class="ci"><div class="circ"><svg width="30" height="40" viewBox="0 0 24 32"><path fill="#fff" d="M12 0a12 12 0 0 0-12 12c0 9 12 20 12 20s12-11 12-20A12 12 0 0 0 12 0zm0 17a5 5 0 1 1 0-10 5 5 0 0 1 0 10z"/></svg></div><p>Brookvale, Elmridge, Carrow Heights<br>Dunmore, North County</p></div>
    <div class="ci"><div class="circ"><svg width="38" height="38" viewBox="0 0 24 24"><path fill="#fff" d="M6.6 10.8a15 15 0 0 0 6.6 6.6l2.2-2.2c.3-.3.7-.4 1-.2 1.1.4 2.3.6 3.6.6.6 0 1 .4 1 1V20c0 .6-.4 1-1 1A17 17 0 0 1 3 4c0-.6.4-1 1-1h3.5c.6 0 1 .4 1 1 0 1.3.2 2.5.6 3.6.1.3 0 .7-.2 1z"/></svg></div><p>Phone:<br><b>555-014-7731</b></p></div>
    <div class="ci"><div class="circ"><svg width="40" height="30" viewBox="0 0 24 18"><rect width="24" height="18" rx="2" fill="#fff"/><path d="M1 2l11 8 11-8" stroke="#e8112d" stroke-width="2" fill="none"/></svg></div><p>Email:<br><b>info@pelmarsteeracademy.com</b></p></div>
  </div>
  <h3>Contact us</h3>
  <div class="cform">
    <div class="inp" style="left:0;top:0;width:428px">👤&nbsp; First Name</div>
    <div class="inp" style="left:449px;top:0;width:428px">👤&nbsp; Last Name</div>
    <div class="inp" style="left:0;top:55px;width:428px">▦&nbsp; Company</div>
    <div class="inp" style="left:0;top:110px;width:428px">✉&nbsp; Email Address</div>
    <div class="inp" style="left:0;top:165px;width:428px">✆&nbsp; Phone Number</div>
    <div class="inp" style="left:449px;top:55px;width:428px;height:158px">✎&nbsp; Message :</div>
  </div>
  <div class="submit"><svg width="18" height="18" viewBox="0 0 24 24"><path fill="#fff" d="M2 11l20-9-7 20-3-8z"/></svg>SUBMIT</div>
</section>

<footer class="footer">
  <h2>Pelmar Steer Academy</h2>
  <div class="socials"><span></span><span></span><span></span><span></span></div>
  <p class="flinks">Home &nbsp;|&nbsp; Teen Courses &nbsp;|&nbsp; Adult Courses &nbsp;|&nbsp; About Us &nbsp;|&nbsp; FAQ &nbsp;|&nbsp; Blog &nbsp;|&nbsp; Requirements</p>
  <p class="flinks">Privacy Policy &nbsp;|&nbsp; Contact us &nbsp;|&nbsp; Terms of Service</p>
  <p class="copy">© 2019 Company Name &nbsp;All right reserved</p>
</footer>

</body>
</html>
```